Plumbing & Heating company

A leaflet containing -

Company name - Brackenfold Plumbing Solutions
logo
Mobile number - 07700 914226
Landline - 01632 870512
Email - Info@brackenfoldplumbing.example.co.uk
website - Brackenfold-plumbing.example.co.uk
Social media logos - pixgram, Chatterly

services we offer

- Boiler replacements (free quote)
- General plumbing & heating
- Tap replacements
- 1st & 2nd
- New builds & Extensions
- Cylinder replcemets

```html
<!DOCTYPE html>
<html lang="en">
<head>
<meta charset="utf-8">
<title>Brackenfold Plumbing Solutions – Leaflet</title>
<link rel="stylesheet" href="https://fonts.googleapis.com/css2?family=Orbitron:wght@700;900&family=Montserrat:wght@400;500;600;700&display=swap">
<style>
:root{
  --blue:#2b66ad;
  --blue-deep:#1f5aa6;
  --red:#f24a35;
  --white:#ffffff;
  --ink:#1d1d1f;
  --copper:#b9714e;
}
*{box-sizing:border-box;margin:0;padding:0}
html,body{width:877px;height:1200px;overflow:hidden;background:#fff}
.leaflet{position:relative;width:877px;height:1200px;overflow:hidden;background:var(--white);font-family:"Montserrat",sans-serif;color:var(--ink)}

.hero-photo{position:absolute;left:0;top:0;width:877px;height:469px;
  background:linear-gradient(120deg,#e9e4dc 0%,#d9cfc2 35%,#3b6fc0 55%,#2d4c84 70%,#c9b7a2 88%,#efe9e1 100%)}
.header{position:absolute;left:0;top:0;width:877px;height:157px;background:var(--white);
  clip-path:polygon(0 0,427px 0,346px 157px,0 157px)}
.brand{position:absolute;left:62px;top:52px;display:flex;align-items:center;gap:10px}
.brand-dot{width:44px;height:44px;border-radius:50%;background:var(--red)}
.brand-name{font-family:"Orbitron",sans-serif;font-weight:900;font-size:17px;line-height:1.2;color:var(--red);letter-spacing:.5px}

.intro{position:absolute;left:0;top:157px;width:877px;height:312px;background:var(--blue);
  clip-path:polygon(0 0,431px 0,607px 312px,0 312px);color:var(--white)}
.intro-title{position:absolute;left:60px;top:74px;font-family:"Orbitron",sans-serif;font-weight:900;font-size:37px;line-height:.98;letter-spacing:.5px}
.intro-title .sub{display:block;font-size:21px;letter-spacing:21px;margin-top:4px}
.intro-text{position:absolute;left:60px;top:210px;width:440px;font-size:15.5px;line-height:1.5;font-weight:500}

.services-band{position:absolute;left:0;top:469px;width:877px;height:94px;background:var(--red);
  display:flex;align-items:center;justify-content:center}
.services-band h2{font-family:"Orbitron",sans-serif;font-weight:900;font-size:34px;color:var(--white);letter-spacing:1px}

.service{position:absolute;width:240px;text-align:center}
.service-icon{width:112px;height:112px;margin:0 auto;position:relative}
.service-icon .ring{position:absolute;inset:0;border-radius:50%;border:5px solid;border-color:var(--blue) var(--blue) var(--red) var(--red);transform:rotate(-20deg)}
.service-icon svg{position:absolute;left:28px;top:28px;width:56px;height:56px;fill:none;stroke:var(--ink);stroke-width:2.4;stroke-linecap:round;stroke-linejoin:round}
.service-label{margin-top:12px;font-size:19px;font-weight:600;line-height:1.2}

.photo-strip{position:absolute;left:0;top:969px;width:877px;height:140px}

.footer{position:absolute;left:0;top:1109px;width:877px;height:91px;background:linear-gradient(180deg,var(--blue) 0%,var(--blue-deep) 100%);color:var(--white);border-top:5px solid var(--red)}
.footer-phones{position:absolute;left:46px;top:18px;font-weight:700;font-size:25px;line-height:1.15}
.footer-row{display:flex;align-items:center;gap:8px}
.footer-row svg{width:20px;height:20px;fill:var(--white)}
.footer-web{position:absolute;left:330px;top:20px;font-size:17px;font-weight:500;line-height:1.55}
.footer-web .footer-row svg{width:16px;height:16px}
.social{position:absolute;left:735px;top:20px;font-size:14px;font-weight:600;line-height:1.7}
.social-item{display:flex;align-items:center;gap:6px}
.social-item span.box{width:14px;height:14px;border:2px solid var(--white);border-radius:3px}
</style>
</head>
<body>
<main class="leaflet">

  <div class="hero-photo" role="img" aria-label="Photo of a plumber in a blue cap fitting a tap on a bathroom basin"></div>

  <header class="header">
    <div class="brand">
      <span class="brand-dot"></span>
      <span class="brand-name">BRACKENFOLD<br>PLUMBING SOLUTIONS</span>
    </div>
  </header>

  <section class="intro">
    <h1 class="intro-title">BRACKENFOLD<br>PLUMBING<span class="sub">SOLUTIONS</span></h1>
    <p class="intro-text">Brackenfold Plumbing &amp; Heating contractor based in Hampshire and covering Winchester and the surrounding areas.</p>
  </section>

  <div class="services-band"><h2>SERVICES WE OFFER</h2></div>

  <!-- Row 1 -->
  <div class="service" style="left:57px;top:593px">
    <div class="service-icon"><span class="ring"></span>
      <svg viewBox="0 0 56 56"><rect x="8" y="14" width="26" height="34" rx="3"/><path d="M21 26c-4 5-4 9 0 9s4-4 0-9z"/><path d="M34 22h8v8h6v10h-6M42 30v10"/><path d="M14 6c2 2-2 4 0 6M20 6c2 2-2 4 0 6"/></svg>
    </div>
    <p class="service-label">Boiler replacements<br>(free quote)</p>
  </div>
  <div class="service" style="left:318px;top:593px">
    <div class="service-icon"><span class="ring"></span>
      <svg viewBox="0 0 56 56"><path d="M12 6v34a10 10 0 0 0 20 0V22a4 4 0 0 1 8 0v28"/><path d="M20 6v34a2 2 0 0 0 4 0V22a12 12 0 0 1 24 0v28"/><path d="M9 6h14M37 50h14"/></svg>
    </div>
    <p class="service-label">General plumbing<br>&amp; heating</p>
  </div>
  <div class="service" style="left:577px;top:593px">
    <div class="service-icon"><span class="ring"></span>
      <svg viewBox="0 0 56 56"><path d="M4 18h14v12H4z"/><path d="M18 20h22a8 8 0 0 1 8 8v4h-8v-4H18"/><path d="M26 20v-6M20 12h12"/><path d="M44 38c-3 4-3 7 0 7s3-3 0-7z"/></svg>
    </div>
    <p class="service-label">Tap replacements</p>
  </div>

  <!-- Row 2 -->
  <div class="service" style="left:57px;top:777px">
    <div class="service-icon"><span class="ring"></span>
      <svg viewBox="0 0 56 56"><path d="M10 10l10 10M8 16l6-6 8 8-6 6zM22 22l18 18"/><path d="M36 36l8 8a4 4 0 0 0 6-6l-8-8"/><path d="M44 8a8 8 0 0 0-10 10L12 40a4 4 0 0 0 6 6l22-22a8 8 0 0 0 10-10l-5 5-5-1-1-5z"/></svg>
    </div>
    <p class="service-label">1st &amp; 2nd</p>
  </div>
  <div class="service" style="left:318px;top:777px">
    <div class="service-icon"><span class="ring"></span>
      <svg viewBox="0 0 56 56"><path d="M16 22l12-10 12 10v14H16z"/><path d="M24 36v-8h8v8"/><path d="M4 28l8 14 10 8M52 28l-8 14-10 8"/></svg>
    </div>
    <p class="service-label">New builds &amp;<br>Extensions</p>
  </div>
  <div class="service" style="left:577px;top:777px">
    <div class="service-icon"><span class="ring"></span>
      <svg viewBox="0 0 56 56"><rect x="16" y="14" width="24" height="36" rx="8"/><path d="M22 14V6h12v8M20 44h16"/><path d="M28 22c-6 7-6 14 0 14s6-7 0-14z"/></svg>
    </div>
    <p class="service-label">Cylinder replcemets</p>
  </div>

  <svg class="photo-strip" viewBox="0 0 877 140" role="img" aria-label="Three photos of copper pipework installations">
    <defs>
      <linearGradient id="copper-a" x1="0" y1="0" x2="1" y2="1"><stop offset="0" stop-color="#8f8a84"/><stop offset=".5" stop-color="#b57652"/><stop offset="1" stop-color="#6e665f"/></linearGradient>
      <linearGradient id="copper-b" x1="0" y1="0" x2="1" y2="0"><stop offset="0" stop-color="#e4e2df"/><stop offset=".5" stop-color="#c58a64"/><stop offset="1" stop-color="#d7d3cf"/></linearGradient>
      <linearGradient id="copper-c" x1="0" y1="0" x2="1" y2="0"><stop offset="0" stop-color="#a36a4b"/><stop offset=".5" stop-color="#d6cfc8"/><stop offset="1" stop-color="#b07150"/></linearGradient>
    </defs>
    <rect width="877" height="140" fill="#fff"/>
    <polygon points="0,4 268,4 322,134 0,134" fill="url(#copper-a)"/>
    <polygon points="290,4 548,4 602,134 344,134" fill="url(#copper-b)"/>
    <polygon points="570,4 877,4 877,134 624,134" fill="url(#copper-c)"/>
    <line x1="278" y1="0" x2="334" y2="140" stroke="#f24a35" stroke-width="4"/>
    <line x1="558" y1="0" x2="614" y2="140" stroke="#f24a35" stroke-width="4"/>
    <rect x="0" y="0" width="877" height="4" fill="#f24a35"/>
  </svg>

  <footer class="footer">
    <div class="footer-phones">
      <div class="footer-row"><svg viewBox="0 0 24 24"><path d="M6.6 10.8a15 15 0 0 0 6.6 6.6l2.2-2.2a1 1 0 0 1 1-.25 11.4 11.4 0 0 0 3.6.57 1 1 0 0 1 1 1V20a1 1 0 0 1-1 1A17 17 0 0 1 3 4a1 1 0 0 1 1-1h3.5a1 1 0 0 1 1 1c0 1.25.2 2.45.57 3.57a1 1 0 0 1-.25 1z"/></svg>07700 914226</div>
      <div class="footer-row"><svg viewBox="0 0 24 24"><path d="M3 8c3-3 15-3 18 0l-2 3-3-1V8H8v2l-3 1z"/><rect x="5" y="12" width="14" height="9" rx="2"/></svg>01632 870512</div>
    </div>
    <div class="footer-web">
      <div class="footer-row"><svg viewBox="0 0 24 24"><path d="M2 5h20v14H2z"/><path d="M2 5l10 8 10-8" fill="none" stroke="#1f5aa6" stroke-width="2"/></svg>Info@brackenfoldplumbing.example.co.uk</div>
      <div class="footer-row"><svg viewBox="0 0 24 24"><circle cx="12" cy="12" r="10"/><path d="M2 12h20M12 2c4 4 4 16 0 20M12 2c-4 4-4 16 0 20" fill="none" stroke="#1f5aa6" stroke-width="1.6"/></svg>www.Brackenfold-plumbing.example.co.uk</div>
    </div>
    <div class="social">
      <div class="social-item"><span class="box"></span>pixgram</div>
      <div class="social-item"><span class="box"></span>Chatterly</div>
    </div>
  </footer>

</main>
</body>
</html>
```